High end Sports Bar/ Restaurant Postcard Design

We are a high end sports bar/restaurant in forest hills on Benning street, we have high quality bar food, 24 draft beers, wine on tap and a great selection of whiskeys & scotches.
What we need is a brightly colored postcard that advertises our weekly events. It must be easy to read but eye-catching and full of fun images that will want to make people come in and drink & eat!
We are called Harlow Commons and have a gastropub feel with one entire wall covered in brick but with 9 t.v's all with audio for all sports games. We are definitely a restaurant too so its not all about sports however we will be carrying the GBX & Coastal Victory League Soccer packages.
On the back of the card we would like to advertise our lunch menu is Monday to Friday 10a.m - 3p.m. Dinner is Sunday - Monday 3p.m - 11p.m and Brunch on Saturday & Sunday. Late night bar menu also available Thursday, Friday & Saturday from 11p.m - 1a.m
Address: 54-16 Benning Street, Forest Hills, N.Y 11382 Phone number: 718 555.0143

Reason: We are extending the deadline to give us time to figure out which design is best for us, thank you all for your participation

Target Market(s)

21 - 45 year olds

Industry/Entity Type

Restaurant

Requirements
Must have
• Each individual days event must be eye-catching yet easy to read.

```html
<!DOCTYPE html>
<html lang="en">
<head>
<meta charset="utf-8">
<title>Harlow Commons – Weekly Events</title>
<link rel="stylesheet" href="https://fonts.googleapis.com/css2?family=Alfa+Slab+One&family=Anton&family=Oswald:wght@200;400;600&family=Great+Vibes&family=Comfortaa:wght@400;700&family=Lobster&display=swap">
<style>
:root{
  --brick:#9a2a22;
  --brick-dark:#6e1a15;
  --bar:#141414;
  --bar-edge:#4a4a4a;
  --white:#ffffff;
  --green:#3f9b3a;
  --blue-top:#4a4fb0;
  --blue-bot:#2f327e;
  --orange:#f2801f;
  --magenta:#a8379e;
  --purple:#6b2c8c;
  --teal:#2c8d97;
  --ink-dark:#2a1a08;
}
*{margin:0;padding:0;box-sizing:border-box}
html,body{width:1200px;height:930px;overflow:hidden;background:var(--brick)}
.card{position:relative;width:1200px;height:930px;overflow:hidden}
.brick-wall{position:absolute;inset:0;background:radial-gradient(ellipse at 50% 40%,var(--brick) 0%,var(--brick-dark) 100%)}
.beer-mug{position:absolute;left:18px;top:0;width:110px;height:140px;border-radius:6px 6px 14px 14px;background:linear-gradient(180deg,#fff7e0 0%,#fff7e0 28%,#f2b233 30%,#d98a12 100%);z-index:3}
.title-bar{position:absolute;left:112px;top:22px;width:1058px;height:170px;background:var(--bar);border-radius:4px;box-shadow:0 6px 14px rgba(0,0,0,.5);z-index:2}
.title-bar::before{content:"";position:absolute;left:60px;right:12px;top:44px;bottom:44px;border:3px solid var(--bar-edge);border-radius:3px}
.title-bar h1{position:absolute;left:0;right:0;top:44px;bottom:44px;display:flex;align-items:center;justify-content:center;padding-left:40px;font-family:"Alfa Slab One",serif;font-weight:400;font-size:64px;letter-spacing:7px;color:var(--white);text-shadow:2px 3px 0 #777;white-space:nowrap}
.event{position:absolute;width:353px;color:var(--white);box-shadow:4px 6px 12px rgba(0,0,0,.45);text-align:center;overflow:hidden}
.row-1{top:235px;height:227px}
.row-2{top:500px;height:226px}
.col-1{left:42px}.col-2{left:415px}.col-3{left:790px}
.monday{background:var(--green);text-align:left;padding:18px 16px}
.monday .head{display:flex;align-items:flex-start;gap:6px}
.monday .day{font-family:"Anton",sans-serif;font-size:44px;line-height:1}
.monday .deal{font-family:"Oswald",sans-serif;font-weight:600;font-size:20px;line-height:1.1}
.monday .price{font-family:"Anton",sans-serif;font-size:92px;line-height:.9;margin-left:auto}
.monday .note{font-family:"Oswald",sans-serif;font-size:16px;line-height:1.35;margin-top:14px}
.tuesday{background:linear-gradient(180deg,var(--blue-top),var(--blue-bot));padding-top:26px}
.tuesday .day{font-family:"Great Vibes",cursive;font-size:74px;line-height:.9}
.tuesday .sub{font-family:"Comfortaa",sans-serif;font-size:30px;line-height:1.1}
.tuesday .big{font-family:"Oswald",sans-serif;font-weight:200;font-size:50px;line-height:1;margin-top:14px;letter-spacing:1px;white-space:nowrap}
.wednesday{background:var(--orange);padding:18px 16px;text-align:left}
.wednesday .head{display:flex;align-items:flex-start}
.wednesday .day{font-family:"Anton",sans-serif;font-size:48px;line-height:1}
.wednesday .trivia{font-family:"Oswald",sans-serif;font-weight:600;font-size:28px;line-height:1.1}
.wednesday .time{margin-left:auto;font-family:"Anton",sans-serif;font-size:64px;line-height:.9;text-align:center}
.wednesday .time small{display:block;font-family:"Oswald",sans-serif;font-size:20px}
.wednesday .desc{font-family:"Comfortaa",sans-serif;font-size:20px;text-align:center;margin-top:28px;line-height:1.3;color:var(--ink-dark)}
.thursday{background:var(--magenta);padding:22px 16px;text-align:left}
.thursday .day{font-family:"Great Vibes",cursive;font-size:74px;line-height:.85}
.thursday .tag{font-family:"Lobster",cursive;font-size:32px;margin-left:16px}
.thursday .foot{display:flex;align-items:flex-end;gap:10px;margin-top:12px}
.thursday .hours{font-family:"Great Vibes",cursive;font-size:44px;line-height:1;white-space:nowrap}
.thursday .offer{font-family:"Oswald",sans-serif;font-size:19px;line-height:1.2;text-align:right}
.weekend{background:var(--purple);padding-top:16px}
.weekend .day{font-family:"Comfortaa",sans-serif;font-size:46px;line-height:1.05}
.weekend .ent{font-family:"Comfortaa",sans-serif;font-weight:700;font-size:28px;margin-top:4px;white-space:nowrap}
.weekend .specials{font-family:"Oswald",sans-serif;font-size:22px;line-height:1.3;margin-top:8px}
.sunday{background:var(--teal);padding-top:28px}
.sunday .day{font-family:"Comfortaa",sans-serif;font-weight:700;font-size:60px;line-height:1}
.sunday .time{font-family:"Comfortaa",sans-serif;font-size:38px}
.sunday .what{font-family:"Comfortaa",sans-serif;font-size:56px;line-height:1}
.food-photo{position:absolute;left:0;right:0;top:732px;bottom:0;background:linear-gradient(90deg,#a8743a 0%,#c77d3a 30%,#b35424 45%,#e8b652 70%,#f1c86a 100%)}
</style>
</head>
<body>
<main class="card">
  <div class="brick-wall" role="img" aria-label="Red brick wall background"></div>
  <div class="beer-mug" role="img" aria-label="Mug of frothy beer"></div>
  <header class="title-bar"><h1>HARLOW COMMONS</h1></header>

  <section class="event monday row-1 col-1">
    <div class="head">
      <div><div class="day">Monday</div><div class="deal">Burger &amp; Beer<br>or Salad &amp; Wine</div></div>
      <div class="price">$10</div>
    </div>
    <p class="note">*choice of HC Burger, Garden Burger<br>&nbsp; or HC Chx Sandwich, Any Salad<br>* Chicken or Steak are additional</p>
  </section>

  <section class="event tuesday row-1 col-2">
    <div class="day">Tuesday</div>
    <div class="sub">Happy Hour</div>
    <div class="big">ALL DAY &amp; NIGHT</div>
  </section>

  <section class="event wednesday row-1 col-3">
    <div class="head">
      <div><div class="day">Wednesday</div><div class="trivia">Trivia Night</div></div>
      <div class="time">8<small>p.m</small></div>
    </div>
    <p class="desc">Come test your knowledge of irrelevant facts &amp; win a prize!</p>
  </section>

  <section class="event thursday row-2 col-1">
    <div class="day">Thursday</div>
    <div class="tag">Ladies Night</div>
    <div class="foot">
      <div class="hours">8p.m-close</div>
      <div class="offer">Ladies drink<br>½ price<br>ALL NIGHT</div>
    </div>
  </section>

  <section class="event weekend row-2 col-2">
    <div class="day">Friday &amp;<br>Saturday</div>
    <div class="ent">live entertainment</div>
    <p class="specials">Food &amp; Drink Specials<br>Every weekend</p>
  </section>

  <section class="event sunday row-2 col-3">
    <div class="day">Sunday</div>
    <div class="time">9 p.m</div>
    <div class="what">karaoke</div>
  </section>

  <div class="food-photo" role="img" aria-label="Photo of a burger, buffalo wings with dip, and french fries"></div>
</main>
</body>
</html>
```